KPT Building And Maintenance

Need a very professional looking double sided Buisiness card with all my details phone number, name, email, license number.

Target Market(s)

construction industry

Industry/Entity Type

building

Contact Information for Business Card

Name Dale Whitcombe. Email Address Info@KPTBuilding.example.au mobile number 0452918730 licence number 871406D. web site

```html
<!DOCTYPE html>
<html lang="en">
<head>
<meta charset="utf-8">
<title>KPT Building And Maintenance – Business Card</title>
<link rel="stylesheet" href="https://fonts.googleapis.com/css2?family=Michroma&family=Roboto:wght@400&display=swap">
<style>
  :root {
    --backdrop: #b3b3b3;
    --charcoal: #4a4a4a;
    --sky: #06a0e3;
    --paper: #ffffff;
  }
  * { margin: 0; padding: 0; box-sizing: border-box; }
  html, body { width: 1000px; height: 1200px; overflow: hidden; background: var(--backdrop); }
  .canvas { position: relative; width: 1000px; height: 1200px; }
  .card { position: absolute; left: 51px; width: 898px; height: 539px; background: var(--paper); overflow: hidden; }
  .card--front { top: 44px; }
  .card--back { top: 617px; }
  .card__shapes { position: absolute; inset: 0; }
  .brand {
    position: absolute;
    display: flex; align-items: center; gap: 14px;
    font-family: "Michroma", sans-serif;
    color: var(--charcoal);
    text-transform: uppercase;
    line-height: 1.25;
  }
  .brand__mark { width: 22px; height: 22px; background: var(--sky); flex: none; }
  .card--front .brand { left: 92px; top: 222px; font-size: 24px; }
  .card--back .brand { left: 216px; top: 218px; font-size: 32px; }
  .card--back .brand__mark { width: 28px; height: 28px; }
  .holder {
    position: absolute; left: 553px; top: 262px;
    font-family: "Michroma", sans-serif; font-size: 21px; font-weight: 400;
    line-height: 1.2; white-space: nowrap;
    color: var(--paper); letter-spacing: 1.5px; text-transform: uppercase;
  }
  .contacts {
    position: absolute; left: 553px; top: 318px;
    list-style: none;
    font-family: "Roboto", sans-serif; font-size: 20px; color: var(--paper);
    white-space: nowrap;
  }
  .contacts li { display: flex; align-items: center; height: 46px; }
  .contacts svg { width: 20px; height: 20px; margin: 0 14px 0 7px; fill: none; stroke: var(--paper); stroke-width: 1.5; flex: none; }
  .contacts .licence { height: 38px; }
</style>
</head>
<body>
<main class="canvas">
  <section class="card card--front">
    <svg class="card__shapes" viewBox="0 0 898 539" aria-hidden="true">
      <rect x="0" y="0" width="898" height="36" fill="var(--charcoal)"/>
      <polygon points="575,36 898,36 898,491 450,491" fill="var(--charcoal)"/>
      <rect x="0" y="503" width="898" height="36" fill="var(--sky)"/>
    </svg>
    <div class="brand"><span class="brand__mark"></span><span>KPT Building<br>And Maintenance</span></div>
    <h1 class="holder">Dale Whitcombe</h1>
    <ul class="contacts">
      <li><svg viewBox="0 0 20 20"><rect x="5" y="2" width="10" height="16" rx="1.5" transform="rotate(25 10 10)"/></svg>0452918730</li>
      <li><svg viewBox="0 0 20 20"><rect x="2" y="4" width="16" height="12"/><path d="M2 4l8 7 8-7M2 16l6-6M18 16l-6-6"/></svg>Info@KPTBuilding.example.au</li>
      <li><svg viewBox="0 0 20 20"><circle cx="10" cy="10" r="8"/><ellipse cx="10" cy="10" rx="3.5" ry="8"/><path d="M2 10h16M4 6h12M4 14h12"/></svg>KPTBuilding.example.au</li>
      <li class="licence">Licence Number 871406D</li>
    </ul>
  </section>

  <section class="card card--back">
    <svg class="card__shapes" viewBox="0 0 898 539" aria-hidden="true">
      <rect x="0" y="0" width="898" height="36" fill="var(--charcoal)"/>
      <polygon points="0,48 190,48 66,539 0,539" fill="var(--sky)"/>
      <rect x="0" y="502" width="898" height="37" fill="var(--sky)"/>
    </svg>
    <div class="brand"><span class="brand__mark"></span><span>KPT Building<br>And Maintenance</span></div>
  </section>
</main>
</body>
</html>
```